Lantern Business Cards

Need business cards for my employees at my restaurant.

Needs to include:
Our Logo
Lantern Bowls & Brews
Name: Nora Pettigrew
Title : Owner
Address: 487 Mirella Ave. Lake Havasu City, AZ 86519
Web: www.lanternkestrel.com
Phone: 928-555-0147
Cell: 928-555-0192
Email: info@lanternkestrel.com

```html
<!DOCTYPE html>
<html lang="en">
<head>
<meta charset="utf-8">
<title>Lantern Business Cards</title>
<link href="https://fonts.googleapis.com/css2?family=Oswald:wght@600&family=Lato:wght@400;700&display=swap" rel="stylesheet">
<style>
  :root {
    --stage: #161616;
    --card: #1f1f20;
    --red: #c0202f;
    --white: #f4f4f4;
    --grey: #d9d9d9;
  }
  * { box-sizing: border-box; margin: 0; padding: 0; }
  html, body { width: 1200px; height: 875px; overflow: hidden; background: var(--stage); }
  .canvas { position: relative; width: 1200px; height: 875px; }

  .card {
    position: absolute;
    width: 520px; height: 300px;
    background: var(--card);
    border-radius: 18px;
    border: 1px solid #2a2a2b;
    border-bottom: 3px solid var(--red);
    border-right: 3px solid var(--red);
    overflow: hidden;
  }
  .card--front { left: 70px; top: 90px; }
  .card--back { left: 610px; top: 480px; }

  .brand { display: flex; align-items: center; gap: 18px; }
  .brand__dot { width: 86px; height: 86px; border-radius: 50%; background: var(--red); flex: none; }
  .brand__name {
    font-family: "Oswald", sans-serif; font-weight: 600;
    color: var(--red); text-transform: uppercase;
    font-size: 62px; line-height: 1; letter-spacing: 2px;
  }
  .brand__tag {
    display: flex; align-items: center; gap: 8px;
    font-family: "Lato", sans-serif; font-size: 11px; letter-spacing: 1.5px;
    color: var(--white); text-transform: uppercase; margin-top: 6px;
  }
  .brand__tag::before, .brand__tag::after { content: ""; height: 1px; width: 40px; background: var(--white); }

  .card--front .brand { position: absolute; left: 70px; top: 100px; }

  .card--back .lockup { position: absolute; left: 34px; top: 34px; }
  .card--back .brand__name { font-size: 44px; }
  .card--back .brand__tag { font-size: 9px; }
  .card--back .brand__tag::before, .card--back .brand__tag::after { width: 26px; }

  .person { position: absolute; left: 34px; top: 118px; }
  .person__name {
    font-family: "Oswald", sans-serif; font-weight: 600; color: var(--red);
    text-transform: uppercase; font-size: 24px; letter-spacing: 1px; line-height: 1.1;
  }
  .person__title { font-family: "Lato", sans-serif; color: var(--white); font-size: 13px; margin-top: 2px; }

  .contact { position: absolute; left: 34px; top: 180px; list-style: none; }
  .contact li {
    display: flex; align-items: flex-start; gap: 9px;
    font-family: "Lato", sans-serif; font-size: 12px; color: var(--white); line-height: 1.45;
  }
  .contact svg { width: 11px; height: 11px; margin-top: 3px; flex: none; fill: var(--red); }

  .mark-area {
    position: absolute; right: 34px; top: 40px;
    width: 210px; height: 210px; border-radius: 50%; background: var(--red);
  }
</style>
</head>
<body>
<main class="canvas">

  <section class="card card--front" aria-label="Card front">
    <div class="brand">
      <span class="brand__dot"></span>
      <div>
        <div class="brand__name">Lantern</div>
        <div class="brand__tag">Bowls and Brews</div>
      </div>
    </div>
  </section>

  <section class="card card--back" aria-label="Card back">
    <div class="lockup">
      <div class="brand__name">Lantern</div>
      <div class="brand__tag">Bowls and Brews</div>
    </div>

    <div class="person">
      <div class="person__name">Nora Pettigrew</div>
      <div class="person__title">Owner</div>
    </div>

    <ul class="contact">
      <li>
        <svg viewBox="0 0 12 12"><path d="M6 0a4 4 0 0 0-4 4c0 3 4 8 4 8s4-5 4-8a4 4 0 0 0-4-4zm0 5.5A1.5 1.5 0 1 1 6 2.5a1.5 1.5 0 0 1 0 3z"/></svg>
        <span>487 Mirella Ave<br>Lake Havasu, AZ 86519</span>
      </li>
      <li>
        <svg viewBox="0 0 12 12"><path d="M2.5 0.5l2 2.5-1.2 1.3c.8 1.7 2 2.9 3.7 3.7L8.3 6.8l2.7 2-.9 2.4C5 11 1 7 .8 2z"/></svg>
        <span>928-555-0147</span>
      </li>
      <li>
        <svg viewBox="0 0 12 12"><path d="M3 0h6a1 1 0 0 1 1 1v10a1 1 0 0 1-1 1H3a1 1 0 0 1-1-1V1a1 1 0 0 1 1-1zm.5 1.5v8h5v-8z"/></svg>
        <span>928-555-0192</span>
      </li>
      <li>
        <svg viewBox="0 0 12 12"><path d="M0 2h12v8H0zm1 1v.3l5 3.2 5-3.2V3z"/></svg>
        <span>info@lanternkestrel.com</span>
      </li>
      <li>
        <svg viewBox="0 0 12 12"><path d="M6 0a6 6 0 1 0 0 12A6 6 0 0 0 6 0zm0 1.2c.7.8 1.2 2 1.3 3.3H4.7C4.8 3.2 5.3 2 6 1.2zM1.3 5.5h2.4c.1 1.3.5 2.5 1.2 3.5a4.8 4.8 0 0 1-3.6-3.5zm3.4 0h2.6c-.1 1.3-.6 2.4-1.3 3.3-.7-.9-1.2-2-1.3-3.3z"/></svg>
        <span>lanternkestrel.com</span>
      </li>
    </ul>

    <div class="mark-area"></div>
  </section>

</main>
</body>
</html>
```